Boracay Wedding Invitation Design

Hello, We would like a wedding invitation design for our wedding in Boracay. We would like it somewhat in the form of a boarding pass with beachy fresh colours, possibly a nice Boracay beach in the background Double sided with an envelope design to match. Maybe something simple on the envelope like a nice picture in the bottom left corner of a shell on a beach or something similar.

I would also like on the opposite side of the invite to be an "information sheet" with a matching beach design

The text files for both sides are included and i have also included 2 designs that i thought looked nice and are similar to what we are after.
Updates

Hello, I have updated the brief to be more specific with text files and images to make it easier for you. Thank you :)

Industry/Entity Type

Wedding

Font styles to use
Decorative
Script

Colors
fbee3d
33a6d7
33b8a4
fbf289
85cae6
ffffff

Requirements
Must have
• I would like to have this quote somewhere on the invitation
• This day I will marry my best friend,
• the one I laugh with,
• live for,
• dream with,
• love
• Owen & Marisa
• Request the pleasure of your company to celebrate their wedding
• On Friday the 17th March 2017
• at
• Velunda Grand Suites
• Boracay, Philippines
• Ceremony begins at 3.00pm
• RSVP
• Owen 0431907254
• Marisa 0417283649
• by
• 17th Jan 2016
• Dress: Beach Formal
• For the "information sheet"
• There will be a 5% discount on rooms booked at the Velunda under the event Owen & Marisa Wedding. The resort has a total of 24 rooms it would be nice if the majority of guests could stay at the resort from the night before until the night after the wedding but if you choose to stay elsewhere on the island there are plenty of other places to stay for cheaper and everything is fairly close as its a small island.
• We have currently blocked room stay for a short period of time so our guests can book rooms. If you choose to do so please email reservations@velundastays.example. Once rooms become available to the public again, towards the end of Jan, it will be first come first served basis. The resort is very popular so im assuming once this happens the rooms will be booked out.
• If you would like to check out the resort itself the website is www.velundagrand-isle.example
• We know its a fair distance to travel but we would really love to see you all there to celebrate and maybe even enjoy a small holiday while your here its a beautiful part of the world.
• If anyone has any questions please feel free to contact Owen on 0431907254
Nice to have
• A nice picture of a Boracay beach in the background would be nice

```html
<!DOCTYPE html>
<html lang="en">
<head>
<meta charset="utf-8">
<title>Owen &amp; Marisa — Wedding Invitation</title>
<link href="https://fonts.googleapis.com/css2?family=Poiret+One&family=Pinyon+Script&family=Arimo:wght@400;700&display=swap" rel="stylesheet">
<style>
  :root {
    --bg: #efe9df;
    --ink: #5b2c14;
    --ink-dark: #111;
    --outline: #2a2a2a;
    --paper: #ffffff;
    --sky: #dce8ec;
    --sea: #86cbc4;
    --sea-deep: #4fb3b0;
    --sand: #eddcbc;
    --sand-light: #f3e8d2;
    --link: #2a6fc0;
    --accent: #d8164f;
  }
  * { box-sizing: border-box; margin: 0; padding: 0; }
  html, body { width: 1200px; height: 1050px; overflow: hidden; background: var(--bg); }
  .canvas { position: relative; width: 1200px; height: 1050px; }

  .ticket { position: absolute; left: 83px; width: 1034px; height: 474px; }
  .ticket--front { top: 39px; }
  .ticket--back { top: 538px; }

  .panel {
    position: absolute; top: 0; height: 100%;
    border: 2px solid var(--outline); border-radius: 12px; overflow: hidden;
    background: var(--paper);
  }
  .panel--stub { left: 0; width: 79px; }
  .panel--main { left: 79px; width: 694px; }
  .panel--side { left: 773px; width: 261px; }

  .beach-scene {
    position: absolute; inset: 0;
    background:
      radial-gradient(ellipse at 30% 65%, rgba(95,150,160,.45) 0 12%, transparent 28%),
      linear-gradient(180deg, var(--sky) 0%, #d2e4e8 18%, #a9d3d0 30%, var(--sea) 42%, #bcdcb0 56%, var(--sand) 72%, var(--sand-light) 100%);
  }
  .beach-scene--stub {
    background: linear-gradient(180deg, #e6e4da 0%, #ece2cd 50%, var(--sand-light) 100%);
  }
  .beach-scene--side {
    background: linear-gradient(180deg, #d6e5ec 0%, #c6dee3 20%, var(--sea) 40%, #9fd3c6 60%, #d4e0a8 85%, #e8e5b4 100%);
  }
  .wash { position: absolute; inset: 0; background: rgba(255,255,255,.28); }

  .stub-title {
    position: absolute; left: 50%; top: 50%;
    transform: translate(-50%, -50%) rotate(-90deg);
    font-family: "Pinyon Script", cursive; font-size: 50px; color: var(--ink);
    white-space: nowrap;
  }

  .invite { position: absolute; left: 0; right: 0; top: 0; text-align: center; color: var(--ink); font-family: "Poiret One", sans-serif; font-size: 21px; }
  .invite .line { position: absolute; left: 0; right: 0; line-height: 30px; }
  .couple {
    position: absolute; left: 0; right: 0; top: 96px;
    font-family: "Pinyon Script", cursive; font-size: 74px; line-height: 100px; color: var(--ink);
  }

  .date-stamp { position: absolute; left: 528px; top: 292px; width: 142px; height: 142px; }

  .side-content { position: absolute; inset: 0; text-align: center; color: var(--ink); }
  .confirmed { position: absolute; top: 34px; left: 0; right: 0; font-family: "Arimo", sans-serif; font-weight: 700; font-size: 19px; color: var(--ink-dark); letter-spacing: .3px; }
  .seat {
    position: absolute; left: 70px; top: 62px; width: 124px; height: 76px;
    background: var(--paper); border: 2px solid #555;
    font-family: "Arimo", sans-serif; font-weight: 700; font-size: 46px; line-height: 72px; color: var(--ink-dark);
  }
  .rsvp { position: absolute; top: 156px; left: 0; right: 0; font-family: "Poiret One", sans-serif; font-size: 21px; line-height: 26.5px; }
  .dress { position: absolute; top: 313px; left: 0; right: 0; font-family: "Poiret One", sans-serif; font-size: 21px; line-height: 26px; }
  .shell { position: absolute; left: 88px; top: 376px; width: 94px; height: 72px; border-radius: 50% 45% 40% 55%; background: radial-gradient(ellipse at 60% 45%, #f2a35a 0 25%, #b7825a 45%, #8b6a52 70%, transparent 72%); }

  .info { position: absolute; left: 83px; top: 28px; width: 550px; font-family: "Arimo", sans-serif; font-size: 14px; line-height: 18px; color: var(--ink-dark); }
  .info h2 { text-align: center; font-size: 15px; font-weight: 700; margin-bottom: 8px; }
  .info p { margin-bottom: 18px; }
  .info a { color: var(--link); text-decoration: underline; }
  .info .contact { padding-left: 16px; }
  .info .contact strong { color: var(--accent); font-weight: 700; }
</style>
</head>
<body>
<main class="canvas">

  <section class="ticket ticket--front">
    <div class="panel panel--stub">
      <div class="beach-scene beach-scene--stub" role="img" aria-label="Faded beach photograph continuing onto the stub"></div>
      <div class="stub-title">Wedding Invitation</div>
    </div>

    <div class="panel panel--main">
      <div class="beach-scene" role="img" aria-label="Photograph of a Boracay beach with palm trees, turquoise sea and a blue outrigger boat on the sand"></div>
      <div class="wash"></div>
      <div class="invite">
        <div class="line" style="top:36px">This day I will marry my best friend,</div>
        <div class="line" style="top:66px">the one I laugh with, live for, dream with, love</div>
        <div class="couple">Owen &amp; Marisa</div>
        <div class="line" style="top:206px">Request the pleasure of your company to celebrate</div>
        <div class="line" style="top:236px">their wedding</div>
        <div class="line" style="top:266px">On Friday the 17th March 2017</div>
        <div class="line" style="top:296px">at</div>
        <div class="line" style="top:326px">Velunda Grand Suites</div>
        <div class="line" style="top:356px">Boracay, Philippines</div>
        <div class="line" style="top:386px">Ceremony begins at 3.00pm</div>
      </div>
      <svg class="date-stamp" viewBox="0 0 142 142" aria-label="Date stamp: March 17th 2017">
        <circle cx="71" cy="71" r="68" fill="none" stroke="#5b2c14" stroke-width="1.5"/>
        <circle cx="71" cy="71" r="60" fill="none" stroke="#5b2c14" stroke-width="1"/>
        <g transform="rotate(-28 71 71)" fill="#5b2c14" font-family="Poiret One, sans-serif" text-anchor="middle">
          <text x="71" y="52" font-size="20">MARCH</text>
          <text x="71" y="90" font-size="40">17TH</text>
          <text x="71" y="114" font-size="20">2017</text>
        </g>
      </svg>
    </div>

    <div class="panel panel--side">
      <div class="beach-scene beach-scene--side" role="img" aria-label="Photograph of the sea and shoreline under a blue sky"></div>
      <div class="wash"></div>
      <div class="side-content">
        <div class="confirmed">CONFIRMED</div>
        <div class="seat">3A</div>
        <div class="rsvp">RSVP<br>Owen 0431907254<br>Marisa 0417283649<br>by<br>17th Jan 2016</div>
        <div class="dress">Dress:<br>Beach Formal</div>
        <div class="shell" role="img" aria-label="Illustration of a conch seashell"></div>
      </div>
    </div>
  </section>

  <section class="ticket ticket--back">
    <div class="panel panel--stub"></div>
    <div class="panel panel--main">
      <div class="info">
        <h2>INFORMATION</h2>
        <p>There will be a 5% discount on rooms booked at the Velunda under the event Owen &amp; Marisa Wedding. The resort has a total of 24 rooms it would be nice if the majority of guests could stay at the resort from the night before until the night after the wedding but if you choose to stay elsewhere on the island there are plenty of other places to stay for cheaper and everything is fairly close as its a small island.</p>
        <p>We have currently blocked room stay for a short period of time so our guests can book rooms. If you choose to do so please email <a>reservations@velundastays.example</a> Once rooms become available to the public again, towards the end of Jan, it will be first come first served basis. The resort is very popular so im assuming once this happens the rooms will be booked out.</p>
        <p>If you would like to check out the resort itself the website is <a>www.velundagrand-isle.example</a></p>
        <p>We know its a fair distance to travel but we would really love to see you all there to celebrate and maybe even enjoy a small holiday while your here its a beautiful part of the world.</p>
        <p class="contact">If anyone has any questions please feel free to contact <strong>Owen on 0431907254</strong></p>
      </div>
    </div>
    <div class="panel panel--side"></div>
  </section>

</main>
</body>
</html>
```